Real Estate Wordpress Landing Page

I'm looking to a landing page dedicated to my real estate brokerage that's catered to promoting that my company provides 1.5% listings to home sellers... I have a couple examples that I'm really looking towards mocking in a version with similar color schemes using my current company colors/website.

http://loftarco.com/
https://www.bluvane.com/about/one-percent-listing-fee

My brokerage company website is http://www.clearhaventa.us/

Target Market(s)

real estate home sellers & buyers

Industry/Entity Type

Real Estate

Coding

Coded - Design and coding required

Number of Pages Required

1 page

Colors
3176b5
0255a3
eaf1f7
cedeed

Requirements
Must have
• Company website colors - http://www.clearhaventa.us/
• Something around the lines of this website page - http://loftarco.com/
• Wordpress compatibility

```html
<!DOCTYPE html>
<html lang="en">
<head>
<meta charset="utf-8">
<title>Clearhaven Realty – List for 1.5% Commission</title>
<link rel="stylesheet" href="https://fonts.googleapis.com/css2?family=Montserrat:wght@400;500;600;700&family=PT+Sans:wght@400;700&display=swap">
<style>
:root{
  --blue:#0255a3;
  --blue-mid:#3176b5;
  --navy:#121a4d;
  --ice:#eaf1f7;
  --mist:#cedeed;
  --ink:#222;
  --muted:#555;
  --white:#fff;
  --head:"Montserrat",sans-serif;
  --body:"PT Sans",sans-serif;
}
*{box-sizing:border-box;margin:0;padding:0}
html,body{width:1200px;height:2378px;overflow:hidden;background:var(--white)}
body{position:relative;font-family:var(--body);color:var(--ink)}
.abs{position:absolute}

/* hero */
.hero-photo{left:0;top:0;width:1200px;height:539px;
  background:linear-gradient(180deg,#3b3f8f 0%,#6d6fb3 35%,#b8b5cf 60%,#77727a 80%,#3c3a3e 100%)}
.brand-box{left:162px;top:0;width:211px;height:106px;background:var(--white);
  display:flex;align-items:center;justify-content:center;gap:10px}
.brand-mark{width:18px;height:18px;background:var(--blue)}
.brand-name{font-family:var(--head);font-weight:600;font-size:19px;color:var(--blue)}
.top-contact{left:700px;top:32px;color:var(--white);font-family:var(--body);font-weight:700;font-size:12px;line-height:23px}
.hero-title{left:162px;top:218px;color:var(--white);font-family:var(--head);font-weight:500;font-size:43px;letter-spacing:.5px}
.hero-sub{left:162px;top:280px;color:var(--white);font-family:var(--head);font-weight:600;font-size:20px}

.lead-form{left:0;top:392px;width:830px;height:147px;background:var(--white)}
.field{position:absolute;border-bottom:2px solid var(--blue);font-size:12px;color:#777;padding-bottom:8px}
.field::before{content:"→ ";color:#888}
.submit{left:645px;top:490px;width:146px;height:38px;border:2px solid var(--blue);
  display:flex;align-items:center;justify-content:center;gap:12px;
  font-weight:700;font-size:12px;color:var(--blue);letter-spacing:.5px}

/* latest property */
.section-title{left:160px;top:650px;font-family:var(--head);font-weight:500;font-size:47px;line-height:60px;color:var(--navy)}
.lead-text{left:162px;top:790px;width:370px;font-size:13.5px;line-height:24px;color:var(--muted)}
.btn{display:flex;align-items:center;justify-content:center;background:var(--blue);color:var(--white);
  font-weight:700;font-size:12px;box-shadow:4px 4px 0 var(--navy);letter-spacing:.3px}
.dots{left:610px;top:713px}
.prop-caption{left:710px;top:620px;font-size:13px;color:#333}
.prop-photo{left:710px;top:644px;width:445px;height:331px;
  background:linear-gradient(160deg,#4f7a3a 0%,#8fae59 40%,#c9cf9a 65%,#bdbdb4 100%)}
.slider-nav{left:1065px;top:940px;width:90px;height:35px;background:var(--white);
  display:flex;align-items:center;justify-content:center;gap:6px}

.statement{left:162px;top:1106px;width:900px;font-family:var(--head);font-weight:600;font-size:28px;line-height:40px;color:var(--navy)}

/* sell block */
.photo-back{left:162px;top:1273px;width:420px;height:404px;background:linear-gradient(180deg,#3d5a2e,#6b7d4f 60%,#4c5b38)}
.photo-front{left:243px;top:1312px;width:404px;height:365px;background:linear-gradient(180deg,#8fb7e2 0%,#c9dcec 35%,#8cae6b 65%,#5f8a3a 100%)}
.photo-label{left:243px;top:1640px;width:404px;height:37px;background:rgba(0,0,0,.35);color:var(--white);font-size:13px;padding:8px 0 0 0}
.sell-title{left:669px;top:1322px;font-family:var(--head);font-weight:500;font-size:22px;color:#111}
.sell-list{left:669px;top:1370px;list-style:none;font-size:13px;line-height:24px;color:#222}
.sell-list li{padding-left:14px;position:relative}
.sell-list li::before{content:"";position:absolute;left:0;top:8px;width:7px;height:7px;border:1.5px solid var(--blue)}
.thumb{position:absolute;top:1514px;width:100px;height:90px}
.view-more{left:596px;top:1652px;font-weight:700;font-size:12px;color:#111}

/* agent */
.agent-band{left:162px;top:1767px;width:876px;height:417px;background:linear-gradient(135deg,#f4f4f4,#dcdcdc 50%,#f0f0f0)}
.agent-photo{left:187px;top:1850px;width:372px;height:269px;background:linear-gradient(180deg,#a9a9a6,#8a8a88 60%,#2b2c34)}
.agent-tag{left:453px;top:1832px;width:165px;height:112px;border:2px solid #111;
  font-family:var(--head);font-size:25px;line-height:32px;color:#111;padding:20px 0 0 14px}
.agent-name{left:658px;top:1840px;width:370px;font-family:var(--head);font-weight:500;font-size:34px;line-height:42px;color:var(--blue)}
.agent-sub{left:658px;top:1940px;font-family:var(--head);font-weight:600;font-size:18px;color:#111}
.agent-text{left:658px;top:1980px;width:370px;font-size:12.5px;line-height:22px;color:#333}

/* footer */
.foot-brand{left:162px;top:2245px;display:flex;align-items:center;gap:8px}
.foot-contact{left:284px;top:2262px;font-size:12px;color:#333}
.foot-email{left:823px;top:2256px;width:215px;border-bottom:1px solid #222;padding-bottom:10px;font-size:12px;color:#333;
  display:flex;justify-content:space-between}
.copyright{left:162px;top:2344px;font-weight:700;font-size:11px;color:#111}
.social{left:935px;top:2344px;display:flex;gap:14px}
.social span{width:12px;height:12px;border-radius:50%;background:var(--blue)}
</style>
</head>
<body>

<section class="hero">
  <div class="abs hero-photo" role="img" aria-label="Modern two-storey white house at dusk with lit windows"></div>
  <div class="abs brand-box"><span class="brand-mark"></span><span class="brand-name">Clearhaven Realty</span></div>
  <div class="abs top-contact">
    <div>Call Us &nbsp;: &nbsp;555-014-2287</div>
    <div>Location : &nbsp;240 Harbor Point Way, Suite 310 Seabrook, FL 33400</div>
  </div>
  <h1 class="abs hero-title">LIST FOR 1.5% COMMISSION</h1>
  <p class="abs hero-sub">And Receive Top Marketing from Listing Pro!</p>

  <form class="abs lead-form">
    <div class="field" style="left:177px;top:40px;width:136px">Name</div>
    <div class="field" style="left:327px;top:40px;width:134px">E-mail</div>
    <div class="field" style="left:476px;top:40px;width:134px">Phone</div>
    <div class="field" style="left:626px;top:40px;width:136px">I'm Interested In</div>
    <div class="field" style="left:177px;top:96px;width:433px">Message</div>
  </form>
  <div class="abs submit">SUBMIT
    <svg width="18" height="16" viewBox="0 0 18 16"><path d="M1 7 17 1 12 15 8 9Z" fill="var(--blue)"/></svg>
  </div>
</section>

<section class="latest">
  <h2 class="abs section-title">Latest<br>Property</h2>
  <p class="abs lead-text">On average, our customers save $5,600 when they list with us... and<br>they still receive top marketing and quality professional service!</p>
  <div class="abs btn" style="left:162px;top:910px;width:105px;height:41px">VIEW MORE</div>
  <svg class="abs dots" width="484" height="317" aria-hidden="true">
    <defs><pattern id="dotgrid" width="21" height="21" patternUnits="userSpaceOnUse"><circle cx="3" cy="3" r="2" fill="#e1e3ea"/></pattern></defs>
    <rect width="484" height="317" fill="url(#dotgrid)"/>
  </svg>
  <p class="abs prop-caption">4120 Maplecrest Lane Lakeview, FL 33460 - $310,000</p>
  <div class="abs prop-photo" role="img" aria-label="Green single-storey home with garage and tropical garden"></div>
  <div class="abs slider-nav">
    <svg width="18" height="18" viewBox="0 0 18 18"><circle cx="9" cy="9" r="7.5" fill="none" stroke="var(--blue)" stroke-width="1.5"/><path d="M13 9H5M8 6 5 9l3 3" fill="none" stroke="var(--blue)" stroke-width="1.5"/></svg>
    <svg width="18" height="18" viewBox="0 0 18 18"><circle cx="9" cy="9" r="7.5" fill="none" stroke="var(--blue)" stroke-width="1.5"/><path d="M5 9h8M10 6l3 3-3 3" fill="none" stroke="var(--blue)" stroke-width="1.5"/></svg>
  </div>
</section>

<p class="abs statement">30 Day Listing Service GUARANTEED. Save thousands $$$ listing with us!Morbi eu sem felis. Integer faucibus ligula vitae enim vestibulum iaculis.</p>

<section class="sell">
  <div class="abs photo-back" role="img" aria-label="Garden and house exterior"></div>
  <div class="abs photo-front" role="img" aria-label="Light blue single-storey home with palm trees and lawn"></div>
  <div class="abs photo-label">218 s Willow Bend drive Fairhaven, FL33461-$550,000</div>
  <h3 class="abs sell-title">SELL WITH CLEARHAVEN &amp; SAVE $$$</h3>
  <ul class="abs sell-list">
    <li>Professional Real Estate Photography</li>
    <li>Complimentary Comparative Market Analysis (CMA)</li>
    <li>FREE Consultation with Real Estate Professional</li>
  </ul>
  <div class="abs btn" style="left:669px;top:1455px;width:95px;height:38px">CALL US</div>
  <div class="abs btn" style="left:777px;top:1455px;width:130px;height:38px">555-014-2287</div>
  <div class="thumb" style="left:598px;background:linear-gradient(180deg,#c7d4de,#9aa596)" role="img" aria-label="House exterior thumbnail"></div>
  <div class="thumb" style="left:703px;background:linear-gradient(180deg,#d9d9d9,#6e6e6e)" role="img" aria-label="Living room interior thumbnail"></div>
  <div class="thumb" style="left:809px;background:linear-gradient(180deg,#8fb3dc,#e2d6a8)" role="img" aria-label="Two-storey house thumbnail"></div>
  <div class="thumb" style="left:914px;background:linear-gradient(180deg,#9ec0e6,#b08b72)" role="img" aria-label="Townhouse thumbnail"></div>
  <div class="abs view-more">VIEW MORE →</div>
</section>

<section class="agent">
  <div class="abs agent-band"></div>
  <div class="abs agent-photo" role="img" aria-label="Portrait of the broker in a dark suit"></div>
  <div class="abs agent-tag">MARCUS<br>DELANE</div>
  <h2 class="abs agent-name">Marcus Delane, Lic. Real Estate Broker</h2>
  <p class="abs agent-sub">CALL US TODAY AND SAVE THOUSANDS $$$</p>
  <p class="abs agent-text">On average, our customers save $5,600 when they list with us...and they still receive top marketing and quality professional service!</p>
  <div class="abs btn" style="left:658px;top:2054px;width:155px;height:38px;gap:10px">
    <svg width="14" height="14" viewBox="0 0 14 14"><path d="M3 1 5.5 4 4 5.5C5 8 6 9 8.5 10L10 8.5 13 11 11.5 13C6 12.5 1.5 8 1 2.5Z" fill="#fff"/></svg>555-014-2287
  </div>
</section>

<footer>
  <div class="abs foot-brand"><span class="brand-mark"></span><span class="brand-name" style="font-size:15px;width:90px;line-height:18px">Clearhaven Realty</span></div>
  <p class="abs foot-contact">555-014-2287 &nbsp;&nbsp;| &nbsp;&nbsp;contact@clearhaventa.us &nbsp;&nbsp;| &nbsp;&nbsp;240 Harbor Point Way, Suite 310 Seabrook, FL 33400</p>
  <div class="abs foot-email">Enter Your Email
    <svg width="18" height="16" viewBox="0 0 18 16"><path d="M1 7 17 1 12 15 8 9Z" fill="#111"/></svg>
  </div>
  <p class="abs copyright">© COPYRIGHT 2018 CLEARHAVENTA.US. ALL RIGHTS RESERVED.</p>
  <div class="abs social" aria-label="Social links"><span></span><span></span><span></span><span></span></div>
</footer>

</body>
</html>
```